Brightfold Partners Website

Brightfold Partners (BP) provide Analytics & Enterprise Performance Management (EPM) advisory & consultancy services. We are passionate about data and making a difference for our clients by working in partnership with them, helping them on their journey to becoming an Brightfold Partner. We deliver insights which give our clients a competitive edge and a much deeper understanding of their organisation.

We need a website which shows who we are, what we do and how we do it.

www.brightfold-partners.example is our very basic website at the moment. We want to completely revamp it with a corporate look

```html
<!DOCTYPE html>
<html lang="en">
<head>
<meta charset="utf-8">
<title>Brightfold Partners – Data Analytics &amp; EPM Consulting</title>
<link href="https://fonts.googleapis.com/css2?family=Fira+Sans:wght@500;600;700&family=Roboto:wght@400;500&display=swap" rel="stylesheet">
<style>
:root{
  --orange:#e0895a;
  --navy:#2c4b60;
  --text:#555d66;
  --muted:#8a9098;
  --hero-bg:#e3edf4;
  --services-bg:#e8ecf0;
  --line:#d7dbe0;
  --white:#ffffff;
}
*{margin:0;padding:0;box-sizing:border-box}
html,body{width:1200px;height:3898px;overflow:hidden}
body{font-family:"Roboto",sans-serif;color:var(--text);background:var(--white);position:relative}
h1,h2,h3,h4,.logo-name{font-family:"Fira Sans",sans-serif;color:var(--navy)}
.abs{position:absolute}
a{color:inherit;text-decoration:none}

/* top bar */
.topbar{top:0;left:0;width:1200px;height:45px;border-bottom:1px solid #eceef0;font-size:14px;color:var(--navy)}
.topbar .item{top:15px;display:flex;align-items:center;gap:8px}
.topbar svg{width:14px;height:14px}
.topbar .sep{left:1053px;top:12px;width:1px;height:20px;background:var(--line)}
.social-dot{top:17px;width:12px;height:12px;background:var(--orange);border-radius:2px}

/* nav */
.nav{top:45px;left:0;width:1200px;height:99px}
.logo{display:flex;align-items:center;gap:12px}
.logo-mark{border-radius:50%;border:7px solid var(--navy)}
.logo-name{font-weight:600;line-height:1.05;letter-spacing:.5px;text-transform:uppercase}
.menu{top:40px;left:531px;display:flex;gap:35px;font-size:15px;color:var(--navy)}
.menu .active{color:var(--orange)}
.icon-btn{top:32px;width:37px;height:37px;border:1.5px solid #222;border-radius:50%;display:flex;align-items:center;justify-content:center}

/* hero */
.hero{top:144px;left:0;width:1200px;height:561px;background:var(--hero-bg)}
.tag{border:1.5px solid var(--orange);color:var(--orange);border-radius:3px;font-size:17px;padding:9px 20px}
.hero h1{top:165px;left:84px;font-size:44px;font-weight:600;line-height:1.2}
.hero p{top:276px;left:86px;width:470px;font-size:16px;line-height:1.45;color:#333}
.btn{background:var(--orange);color:#fff;border-radius:25px;font-size:15px;font-weight:500;display:flex;align-items:center;justify-content:center;gap:10px}
.play{border-radius:50%;display:flex;align-items:center;justify-content:center}
.photo{role:img}
.hero-photo{top:0;left:599px;width:601px;height:561px;background:linear-gradient(135deg,#dfe6ec 0%,#b9c6d1 45%,#7d8d99 100%)}

/* about */
.eyebrow{color:var(--orange);font-size:15px;display:flex;align-items:center;gap:12px}
.eyebrow .dash{display:inline-block;width:28px;height:2px;background:var(--orange)}
.about h2{font-size:38px;font-weight:600;line-height:1.15}
.about p{font-size:14px;line-height:1.55;color:#555}
.btn-outline{border:1.5px solid var(--orange);color:var(--orange);border-radius:25px;font-size:15px;display:flex;align-items:center;justify-content:center}

/* services */
.services{top:1419px;left:0;width:1200px;height:722px;background:linear-gradient(135deg,#eceff2 0%,#e2e7ec 50%,#eef1f3 100%)}
.services h2{font-size:38px;font-weight:600}
.card{top:279px;width:326px;height:313px;background:#fff;text-align:center}
.card-icon{top:-46px;left:118px;width:90px;height:90px;background:var(--orange);display:flex;align-items:center;justify-content:center}
.card-icon:after{content:"";position:absolute;bottom:-14px;left:33px;border-left:12px solid transparent;border-right:12px solid transparent;border-top:14px solid var(--orange)}
.card h3{margin-top:86px;font-size:20px;font-weight:600;line-height:1.35}
.card p{margin:14px auto 0;width:256px;font-size:14px;line-height:1.5;color:#666}
.card .more{display:inline-block;margin-top:16px;font-size:14px;font-weight:500;color:var(--navy)}

/* process */
.process{top:2141px;left:0;width:1200px;height:613px}
.process h2{top:156px;width:1200px;text-align:center;font-size:38px;font-weight:600}
.step{top:293px;width:300px}
.step .num{width:50px;height:50px;border-radius:50%;background:var(--orange);position:absolute;left:0;top:0}
.step .num span{position:absolute;left:34px;top:18px;font-family:"Fira Sans",sans-serif;font-size:34px;font-weight:600;color:var(--navy)}
.step h4{position:absolute;left:73px;top:0;font-size:21px;font-weight:600;line-height:1.35}
.step p{position:absolute;left:0;top:87px;width:330px;font-size:14px;line-height:1.6;color:#666}

/* contact */
.contact{top:2754px;left:0;width:1200px;height:674px;background:linear-gradient(110deg,#dde4ea 0%,#c7d1da 40%,#9aa8b4 75%,#707e8a 100%)}
.form-card{top:128px;left:86px;width:586px;height:413px;background:#fff}
.form-card h2{position:absolute;left:42px;top:44px;font-size:36px;font-weight:600;display:flex;align-items:center;gap:12px}
.form-card h2 .dash{width:28px;height:2px;background:var(--orange)}
.field{position:absolute;height:30px;border-bottom:1px solid var(--line);font-size:13px;color:var(--muted);padding-top:5px}
.send{position:absolute;left:42px;top:319px;width:108px;height:40px}

/* footer */
.footer{top:3428px;left:0;width:1200px;height:470px}
.footer h4{font-size:20px;font-weight:600}
.footer p,.footer li{font-size:13.5px;color:#444;line-height:1.55}
.footer ul{list-style:none}
.footer li{margin-bottom:12px;display:flex;gap:14px}
.footer li:before{content:"»";color:var(--muted)}
.soc{top:3718px;width:42px;height:42px;background:var(--navy)}
.copyright{top:3842px;width:1200px;text-align:center;font-size:14px;color:#555}
.copyright a{color:var(--orange)}
</style>
</head>
<body>

<!-- top bar -->
<div class="abs topbar">
  <div class="abs item" style="left:86px">
    <svg viewBox="0 0 24 24"><path fill="#e0895a" d="M6.6 10.8a15 15 0 0 0 6.6 6.6l2.2-2.2c.3-.3.7-.4 1-.2 1.1.4 2.3.6 3.6.6.6 0 1 .4 1 1V20c0 .6-.4 1-1 1A17 17 0 0 1 3 4c0-.6.4-1 1-1h3.5c.6 0 1 .4 1 1 0 1.3.2 2.5.6 3.6.1.3 0 .7-.2 1z"/></svg>
    <span>01 555 0142</span>
  </div>
  <div class="abs item" style="left:216px">
    <svg viewBox="0 0 24 24"><rect x="2" y="5" width="20" height="14" rx="1" fill="#e0895a"/><path d="M2 6l10 7 10-7" stroke="#fff" stroke-width="1.6" fill="none"/></svg>
    <span>hello@brightfold-partners.example</span>
  </div>
  <div class="abs item" style="left:645px">
    <svg viewBox="0 0 24 24"><path fill="#e0895a" d="M12 2a7 7 0 0 0-7 7c0 5 7 13 7 13s7-8 7-13a7 7 0 0 0-7-7zm0 9.5a2.5 2.5 0 1 1 0-5 2.5 2.5 0 0 1 0 5z"/></svg>
    <span>12 Harbour Row, Northgate, Eastbridge 4, E04 KT21</span>
  </div>
  <div class="abs sep"></div>
  <div class="abs social-dot" style="left:1075px"></div>
  <div class="abs social-dot" style="left:1100px"></div>
</div>

<!-- navigation -->
<header class="abs nav">
  <div class="abs logo" style="left:86px;top:18px">
    <div class="logo-mark" style="width:62px;height:62px"></div>
    <div class="logo-name" style="font-size:22px">Brightfold<br>Partners</div>
  </div>
  <nav class="abs menu">
    <a class="active">Home</a><a>Who We Are</a><a>What We Do</a><a>How We Do</a><a>Contact</a>
  </nav>
  <div class="abs icon-btn" style="left:1023px">
    <svg width="14" height="14" viewBox="0 0 24 24"><circle cx="10" cy="10" r="6.5" stroke="#222" stroke-width="2.5" fill="none"/><path d="M15 15l6 6" stroke="#222" stroke-width="2.5"/></svg>
  </div>
  <div class="abs icon-btn" style="left:1074px">
    <svg width="18" height="14" viewBox="0 0 18 14"><path d="M1 2h16M1 7h11M1 12h16" stroke="#222" stroke-width="2"/></svg>
  </div>
</header>

<!-- hero -->
<section class="abs hero">
  <div class="abs tag" style="left:85px;top:108px">Brightfold Partners</div>
  <h1 class="abs">Data Analytics &amp;<br>Epm Consulting Services</h1>
  <p class="abs">BP are a Data Analytics &amp; EPM company, specialising in the implementation and support of Business Intelligence, EPM and Data Analytics business solutions, both in the Cloud and on-premise.</p>
  <a class="abs btn" style="left:85px;top:390px;width:157px;height:47px">Get Started
    <svg width="20" height="20" viewBox="0 0 20 20"><circle cx="10" cy="10" r="8.5" stroke="#fff" stroke-width="1.5" fill="none"/><path d="M6 10h7M10 7l3 3-3 3" stroke="#fff" stroke-width="1.5" fill="none"/></svg>
  </a>
  <div class="abs play" style="left:253px;top:382px;width:60px;height:60px;background:#c9d5de">
    <div class="play" style="width:44px;height:44px;background:var(--navy)">
      <svg width="12" height="12" viewBox="0 0 12 12"><path d="M2 1l9 5-9 5z" fill="#e0895a"/></svg>
    </div>
  </div>
  <div class="abs" style="left:330px;top:404px;font-size:15px;color:var(--navy)">Watch Our Video</div>
  <div class="abs hero-photo" role="img" aria-label="Photo of analysts reviewing financial charts on a laptop and printed reports"></div>
</section>

<!-- about -->
<section class="about">
  <div class="abs" role="img" aria-label="Photo of a hand pointing at data analysis on a tablet screen" style="left:86px;top:902px;width:314px;height:386px;background:linear-gradient(160deg,#1a2f7a 0%,#2458c8 55%,#1b3a9a 100%)"></div>
  <div class="abs" role="img" aria-label="Photo of a support consultant wearing a headset" style="left:324px;top:837px;width:251px;height:271px;background:linear-gradient(135deg,#f2efe9 0%,#d8d2c9 60%,#a79d92 100%);border-left:14px solid #fff;border-bottom:14px solid #fff;box-sizing:content-box;margin-left:-14px"></div>
  <div class="abs play" style="left:275px;top:1001px;width:80px;height:80px;background:rgba(255,255,255,.85)">
    <div class="play" style="width:52px;height:52px;background:#8c1d1d">
      <svg width="16" height="16" viewBox="0 0 12 12"><path d="M3 1l8 5-8 5z" fill="#fff"/></svg>
    </div>
  </div>
  <div class="abs eyebrow" style="left:622px;top:889px">Who We Are <span class="dash"></span></div>
  <h2 class="abs" style="left:621px;top:918px">Welcome to<br>Brightfold Partners</h2>
  <p class="abs" style="left:622px;top:1016px;width:455px">Brightfold Partners is an exciting start-up in the Data Analytics and EPM space.&nbsp; Founded in 2019, BP specialise in the implementation and support of BI, EPM and Data Analytics business solutions, both in the Cloud and on-premise.</p>
  <p class="abs" style="left:622px;top:1118px;width:460px">Call us on 01 555 0142 or email: hello@brightfold-partners.example for more information</p>
  <a class="abs btn-outline" style="left:621px;top:1182px;width:159px;height:49px">Get Free Quote</a>
  <div class="abs" style="left:802px;top:1191px;width:156px;height:32px;background:#eef0f2;border-radius:3px" role="img" aria-label="Technology partner badge"></div>
</section>

<!-- services -->
<section class="abs services">
  <div class="abs eyebrow" style="left:85px;top:126px">What We Do <span class="dash"></span></div>
  <h2 class="abs" style="left:85px;top:148px">Our Services</h2>
  <p class="abs" style="left:590px;top:125px;width:525px;font-size:14px;line-height:1.55;color:#555">We are passionate about data and making a difference for our clients by working in partnership with them, helping them on their journey to becoming an Brightfold Partner.</p>

  <div class="abs card" style="left:86px">
    <div class="abs card-icon"><svg width="50" height="46" viewBox="0 0 50 46" fill="none" stroke="#fff" stroke-width="2"><rect x="14" y="3" width="26" height="17" rx="3"/><path d="M20 20l-3 5 8-5"/><path d="M20 11h14"/><path d="M3 32h8l8-4h10a3 3 0 0 1 0 6H20M11 40l10 2 17-10a3 3 0 0 0-3-5"/></svg></div>
    <h3>Advise &amp;<br>Architect services</h3>
    <p>Helping our customers understand the art of the possible and safeguarding their investments by overseeing implementations.</p>
    <a class="more">Learn More &nbsp;»</a>
  </div>
  <div class="abs card" style="left:437px">
    <div class="abs card-icon"><svg width="48" height="48" viewBox="0 0 48 48" fill="none" stroke="#fff" stroke-width="2"><rect x="5" y="6" width="34" height="36"/><path d="M12 30l8-8 6 6 8-12"/><path d="M40 4l5 5-18 18-6 1 1-6z"/></svg></div>
    <h3>Design<br>&amp; Implement</h3>
    <p>Working with the project management team, through each stage of the project, with clearly defined deliverables and well exercised plans to deliver them.</p>
    <a class="more">Learn More &nbsp;»</a>
  </div>
  <div class="abs card" style="left:788px">
    <div class="abs card-icon"><svg width="48" height="48" viewBox="0 0 48 48" fill="none" stroke="#fff" stroke-width="2"><circle cx="24" cy="24" r="15"/><path d="M24 3v6M24 39v6M3 24h6M39 24h6M9 9l4 4M35 35l4 4M39 9l-4 4M13 35l-4 4"/><path d="M19 20l-4 4 4 4M29 20l4 4-4 4M26 18l-4 12"/></svg></div>
    <h3>Optimise &amp;<br>Manage</h3>
    <p>Our Managed Services delivers proactive, on-demand support for EPM and Data Analytics environments</p>
    <a class="more">Learn More &nbsp;»</a>
  </div>
</section>

<!-- process -->
<section class="abs process">
  <div class="abs eyebrow" style="left:0;top:129px;width:1200px;justify-content:center"><span class="dash"></span>How We Do It<span class="dash"></span></div>
  <h2 class="abs">Our Working Process</h2>
  <svg class="abs" style="left:280px;top:243px" width="170" height="30" viewBox="0 0 170 30" fill="none" stroke="#a9aeb3" stroke-width="3"><path d="M5 25C50 8 110 5 155 14" stroke-dasharray="12 8"/><path d="M145 7l12 7-12 6"/></svg>
  <svg class="abs" style="left:693px;top:453px" width="170" height="30" viewBox="0 0 170 30" fill="none" stroke="#a9aeb3" stroke-width="3"><path d="M5 5C50 22 110 22 155 15" stroke-dasharray="12 8"/><path d="M144 8l12 7-11 7"/></svg>
  <div class="abs step" style="left:85px"><div class="num"><span>1</span></div><h4>Lorem Ipsum<br>Step1</h4><p>Lorem ipsum dolor sit amet, consectetur adipiscing elit. Aenean venenatis leo quis mauris efficitur ultrices.</p></div>
  <div class="abs step" style="left:436px"><div class="num"><span>2</span></div><h4>Lorem Ipsum<br>Step2</h4><p>Lorem ipsum dolor sit amet, consectetur adipiscing elit. Aenean venenatis leo quis mauris efficitur ultrices.</p></div>
  <div class="abs step" style="left:787px"><div class="num"><span>3</span></div><h4>Lorem Ipsum<br>Step 3</h4><p>Lorem ipsum dolor sit amet, consectetur adipiscing elit. Aenean venenatis leo quis mauris efficitur ultrices.</p></div>
</section>

<!-- contact -->
<section class="abs contact" role="img" aria-label="Photo of a smiling professional in a bright office with colleagues behind">
  <div class="abs form-card">
    <h2>Get in touch <span class="dash"></span></h2>
    <div class="field" style="left:42px;top:112px;width:245px">First name*</div>
    <div class="field" style="left:299px;top:112px;width:245px">Last name*</div>
    <div class="field" style="left:42px;top:162px;width:245px">Phone number*</div>
    <div class="field" style="left:299px;top:162px;width:245px">Email*</div>
    <div class="field" style="left:42px;top:212px;width:502px;height:72px">Message</div>
    <a class="btn send">Send Now</a>
  </div>
</section>

<!-- footer -->
<footer>
  <div class="abs logo" style="left:86px;top:3575px">
    <div class="logo-mark" style="width:48px;height:48px;border-width:5px"></div>
    <div class="logo-name" style="font-size:17px">Brightfold<br>Partners</div>
  </div>
  <p class="abs" style="left:88px;top:3640px;width:270px;font-size:13.5px;color:#444;line-height:1.55">We deliver insights which give our clients a competitive edge and a much deeper understanding of their organisation.</p>
  <div class="abs soc" style="left:86px"></div>
  <div class="abs soc" style="left:143px"></div>

  <div class="abs footer" style="top:3428px">
    <h4 class="abs" style="left:417px;top:134px">Main Menu</h4>
    <ul class="abs" style="left:417px;top:186px"><li>Home</li><li>Who We Are</li><li>What We Do</li><li>How We Do</li><li>Contact</li></ul>
    <h4 class="abs" style="left:597px;top:134px">Our Services</h4>
    <ul class="abs" style="left:597px;top:186px"><li>Advise &amp; Architect</li><li>Design &amp; Implement</li><li>Optimise &amp; Manage</li></ul>
    <h4 class="abs" style="left:823px;top:134px">Contact</h4>
    <p class="abs" style="left:823px;top:186px">Call : 01 555 0142</p>
    <p class="abs" style="left:823px;top:219px">Email : hello@brightfold-partners.example</p>
    <p class="abs" style="left:823px;top:252px;width:300px">Location : 12 Harbour Row, Northgate, Eastbridge 4, E04 KT21</p>
  </div>
  <div class="abs" style="left:86px;top:3813px;width:1028px;height:1px;background:var(--line)"></div>
  <div class="abs copyright">Copyright © 2022 <a>Brightfold-Partners.</a>All Rights Reserved.</div>
</footer>

</body>
</html>
```